Landscape design build company door flyer

I would like this flyer to convey a high-level of professionalism for a company that is excellent with communication with their clients as well as a company that does incredible installations

Went on vacation/holiday

```html
<!DOCTYPE html>
<html lang="en">
<head>
<meta charset="utf-8">
<title>Greenmere Landscapes – Flyer</title>
<link rel="stylesheet" href="https://fonts.googleapis.com/css2?family=Montserrat:wght@500;600;700;800&display=swap">
<style>
  :root {
    --navy: #13334a;
    --leaf: #178a16;
    --hedge-light: #5fbf2a;
    --hedge-mid: #2f9a1c;
    --hedge-dark: #1c5e14;
    --sun: #fff6dc;
    --white: #ffffff;
  }
  * { box-sizing: border-box; margin: 0; padding: 0; }
  html, body { width: 840px; height: 1200px; overflow: hidden; background: #f3f3f3; }
  .flyer {
    position: relative;
    width: 840px;
    height: 1200px;
    overflow: hidden;
    background: var(--white);
    font-family: "Montserrat", sans-serif;
  }
  .hero-photo {
    position: absolute; inset: 0 0 auto 0; height: 560px;
    background:
      radial-gradient(circle at 88% 8%, var(--sun) 0%, rgba(255,240,200,.85) 12%, rgba(190,220,90,.4) 30%, transparent 48%),
      linear-gradient(100deg, var(--hedge-dark) 0%, var(--hedge-mid) 30%, var(--hedge-light) 60%, #9fcf45 85%, #e8e2b0 100%);
  }
  .panel { position: absolute; left: 0; top: 0; width: 840px; height: 1072px; }
  .brand {
    position: absolute; left: 612px; top: 40px; width: 200px;
    text-align: center; color: var(--navy);
    font-family: "Montserrat", sans-serif; font-weight: 600;
  }
  .brand-dot {
    width: 44px; height: 44px; border-radius: 50%;
    background: var(--navy); margin: 0 auto 12px;
  }
  .brand-name { font-size: 15px; letter-spacing: .4px; line-height: 1.2; white-space: nowrap; }
  .brand-tag { font-size: 8px; letter-spacing: .5px; margin-top: 3px; white-space: nowrap; }
  .section-label {
    position: absolute; left: 91px; height: 36px; padding: 0 11px;
    background: var(--leaf); color: var(--white);
    font-weight: 700; font-size: 19px; letter-spacing: 1.4px;
    line-height: 36px; border-radius: 8px 0 8px 0;
  }
  .section-text {
    position: absolute; left: 91px; width: 669px;
    color: var(--white); font-weight: 500; font-size: 18.5px;
    line-height: 28.5px; letter-spacing: 1.1px;
  }
  .section-text .line { display: block; text-align: justify; text-align-last: justify; }
  .section-text .line:last-child { text-align-last: left; }
  .about-label { top: 627px; }
  .about-text { top: 684px; }
  .services-label { top: 853px; }
  .services-text { top: 911px; }
  .contact-band {
    position: absolute; left: 0; top: 1064px; width: 840px; height: 48px;
    border-top: 3px solid var(--white);
    background: var(--leaf); color: var(--white);
    text-align: center; font-weight: 800; font-size: 25px;
    letter-spacing: 2px; line-height: 44px;
  }
  .contact-list {
    position: absolute; left: 0; top: 1112px; width: 840px; height: 88px;
    display: flex; justify-content: center; align-items: center; gap: 26px;
    color: var(--navy); font-weight: 700; font-size: 18px; letter-spacing: .6px;
    list-style: none;
  }
  .contact-list li { display: flex; align-items: center; gap: 8px; white-space: nowrap; }
  .contact-list svg { width: 24px; height: 24px; fill: none; stroke: var(--navy); stroke-width: 1.6; }
</style>
</head>
<body>
<main class="flyer">
  <div class="hero-photo" role="img" aria-label="Rows of clipped green hedges lit by warm sunlight"></div>

  <svg class="panel" viewBox="0 0 840 1072">
    <defs>
      <radialGradient id="hedgeFade" cx="0.85" cy="0.55" r="0.6">
        <stop offset="0" stop-color="#3f9a2a"/>
        <stop offset="0.6" stop-color="#2a7a22"/>
        <stop offset="1" stop-color="#1d5a22"/>
      </radialGradient>
      <linearGradient id="navyFade" x1="0" y1="0" x2="1" y2="0.25">
        <stop offset="0.38" stop-color="#13334a" stop-opacity="1"/>
        <stop offset="0.62" stop-color="#13334a" stop-opacity="0.55"/>
        <stop offset="0.9" stop-color="#13334a" stop-opacity="0.05"/>
      </linearGradient>
      <clipPath id="panelShape">
        <path d="M0,512 C260,440 520,380 840,364 L840,1072 L0,1072 Z"/>
      </clipPath>
    </defs>
    <g clip-path="url(#panelShape)">
      <rect x="0" y="350" width="840" height="722" fill="url(#hedgeFade)" role="img" aria-label="Garden path lined with round green shrubs"/>
      <rect x="0" y="350" width="840" height="722" fill="url(#navyFade)"/>
    </g>
    <path d="M0,512 C260,440 520,380 840,364" fill="none" stroke="#ffffff" stroke-width="4"/>

    <g role="img" aria-label="Curved pool bordered by sculpted hedges">
      <circle cx="180" cy="453" r="99" fill="#4ea846" stroke="#ffffff" stroke-width="5"/>
      <circle cx="180" cy="453" r="58" fill="#5fb8c8" opacity=".55"/>
    </g>
    <g role="img" aria-label="Garden house with trees and stone seating">
      <circle cx="419" cy="388" r="99" fill="#6b8a4e" stroke="#ffffff" stroke-width="5"/>
    </g>
    <g role="img" aria-label="Lawn edged with rounded shrubs in sunlight">
      <circle cx="658" cy="352" r="99" fill="#7dbd3a" stroke="#ffffff" stroke-width="5"/>
    </g>
  </svg>

  <div class="brand">
    <div class="brand-dot"></div>
    <div class="brand-name">GREENMERE LANDSCAPES</div>
    <div class="brand-tag">GARDEN &amp; HARDSCAPE DESIGN</div>
  </div>

  <h2 class="section-label about-label">ABOUT US</h2>
  <p class="section-text about-text">
    <span class="line">Lorem ipsum dolor sit amet, consectetur adipiscing elit, sed</span>
    <span class="line">do eiusmod tempor incididunt ut labore et dolore magna</span>
    <span class="line">aliqua. Quis ipsum suspendisse ultrices gravida. Risus</span>
    <span class="line">commodo viverra maecenas accumsan lacus vel facilisis.</span>
  </p>

  <h2 class="section-label services-label">OUR SERVICES</h2>
  <p class="section-text services-text">
    <span class="line">Quis ipsum suspendisse ultrices gravida. Risus commodo</span>
    <span class="line">viverra maecenas accumsan lacus vel facilisis. Lorem ipsum</span>
    <span class="line">dolor sit amet, consectetur adipiscing elit, sed do eiusmod</span>
    <span class="line">tempor incididunt ut labore et dolore magna aliqua.</span>
  </p>

  <div class="contact-band">CONTACT US</div>
  <ul class="contact-list">
    <li>
      <svg viewBox="0 0 24 24"><path d="M5 3h4l2 5-2.5 1.5a11 11 0 0 0 6 6L16 13l5 2v4a2 2 0 0 1-2 2A17 17 0 0 1 3 5a2 2 0 0 1 2-2z"/></svg>
      +123 4567890
    </li>
    <li>
      <svg viewBox="0 0 24 24"><rect x="2.5" y="5" width="19" height="14"/><path d="M2.5 5l9.5 8 9.5-8M2.5 19l7-6.5M21.5 19l-7-6.5"/></svg>
      info@email.com
    </li>
    <li>
      <svg viewBox="0 0 24 24"><circle cx="12" cy="12" r="9.5"/><ellipse cx="12" cy="12" rx="4.2" ry="9.5"/><path d="M2.5 12h19M4 7h16M4 17h16"/></svg>
      www.greenmerelandscapes.com
    </li>
  </ul>
</main>
</body>
</html>
```